BrightArc Orthodontics appointment card design

I need appointment cards/ business cards made. Front will be Logo, name, title, email, phone number and location (5327 Varden Hollow Blvd, Ste 412, Concord, NC 28027) . the back should have an appointment card (name, time, date) and also 3 addresses listed with a check box so we can check to which location they are going.
Wendell Pratt Orthodontics
- 6315 Elmore Street, Ste 514, Harrisburg, NC 28075
- 3761 Tessaly Drive NE, Ste 118, Concord, NC 28025
- 2194 Quarrow Medical Drive, Ste 605, Charlotte, NC 28277
Business card can be horizontal or vertical in Design.
I need to be able to edit it to update and add new employees

Requirements
Must have
• Front:
• - Logo
• - Name & Title (able to be edited)
• - phone (704-555-0148) & Email (need to be able to edit)
• - Address: 5327 Varden Hollow Blvd, Ste 412
• Concord, NC 28027
• Back:
• Appointment Card design:
• - Name, time, Date
• - 3 locations w/ a check box so the patient knows where to go:
• Wendell Pratt Orthodontics
• - 6315 Elmore Street, Ste 514, Harrisburg, NC 28075
• - 3761 Tessaly Drive NE, Ste 118, Concord, NC 28025
• - 2194 Quarrow Medical Drive, Ste 605, Charlotte, NC 28277

```html
<!DOCTYPE html>
<html lang="en">
<head>
<meta charset="utf-8">
<title>BrightArc Orthodontics – Appointment / Business Card</title>
<link href="https://fonts.googleapis.com/css2?family=Montserrat:wght@600;700;800&family=Roboto:wght@400;500&display=swap" rel="stylesheet">
<style>
  :root{
    --page:#2b2c2e;
    --blue:#1378c0;
    --blue-deep:#0b5fa8;
    --blue-light:#1d8bd3;
    --grey-band:#5f6266;
    --ink:#161616;
    --white:#ffffff;
    --paper:#f7f7f7;
  }
  *{box-sizing:border-box;margin:0;padding:0}
  html,body{width:1200px;height:900px;overflow:hidden;background:var(--page)}
  .canvas{position:relative;width:1200px;height:900px}
  .card{position:absolute;left:290px;width:620px;height:355px;border-radius:22px;overflow:hidden}

  /* ---------- back: appointment ---------- */
  .card-back{top:55px;background:linear-gradient(135deg,var(--blue-light),var(--blue-deep));color:var(--white);font-family:"Roboto",sans-serif}
  .appt-title{position:absolute;left:34px;top:32px;font-family:"Montserrat",sans-serif;font-weight:700;font-size:15px;letter-spacing:.5px}
  .back-brand{position:absolute;right:36px;top:26px;text-align:right;font-family:"Montserrat",sans-serif;font-weight:700;font-size:20px;line-height:1.05}
  .field-label{position:absolute;font-size:13px}
  .field{position:absolute;height:30px;background:var(--white);border-radius:15px;color:var(--blue);font-size:14px;display:flex;align-items:center;justify-content:space-around;padding:0 40px}
  .label-name{left:34px;top:100px}
  .field-name{left:92px;top:93px;width:490px}
  .label-date{left:34px;top:143px}
  .field-date{left:92px;top:136px;width:250px}
  .label-time{left:360px;top:143px}
  .field-time{left:404px;top:136px;width:178px}
  .practice{position:absolute;left:34px;top:194px;font-family:"Montserrat",sans-serif;font-weight:700;font-size:15px}
  .locations{position:absolute;left:34px;top:222px;list-style:none;font-size:14px;line-height:24px}
  .locations li{display:flex;align-items:center;gap:8px}
  .locations svg{width:13px;height:13px;flex:none}
  .check-dots{position:absolute;right:34px;bottom:26px;display:flex;flex-direction:column;gap:8px}
  .check-dots span{width:26px;height:26px;border-radius:50%;background:var(--white)}

  /* ---------- front: business card ---------- */
  .card-front{top:470px;background:var(--paper);font-family:"Roboto",sans-serif;color:var(--ink)}
  .card-front .waves{position:absolute;inset:0}
  .front-brand{position:absolute;left:44px;top:138px;font-family:"Montserrat",sans-serif;font-weight:700;font-size:34px;line-height:1.05;color:var(--blue)}
  .divider{position:absolute;left:300px;top:118px;width:1.5px;height:150px;background:#8a8a8a}
  .person{position:absolute;left:326px;top:118px}
  .person-name{font-family:"Montserrat",sans-serif;font-weight:800;font-size:20px;letter-spacing:.5px}
  .person-title{font-family:"Montserrat",sans-serif;font-weight:600;font-size:14px;color:var(--blue);margin-top:2px}
  .person-address{font-size:15px;line-height:20px;margin-top:8px}
  .contact{display:flex;align-items:center;gap:10px;font-size:16px;margin-top:7px}
  .contact svg{width:22px;height:22px;flex:none}
</style>
</head>
<body>
<main class="canvas">

  <section class="card card-back" aria-label="Appointment card, back">
    <h2 class="appt-title">APPOINTMENT</h2>
    <div class="back-brand">BrightArc<br>Orthodontics</div>
    <span class="field-label label-name">Name</span>
    <div class="field field-name"></div>
    <span class="field-label label-date">Date</span>
    <div class="field field-date"><span>/</span><span>/</span></div>
    <span class="field-label label-time">Time</span>
    <div class="field field-time"><span>:</span></div>

    <h3 class="practice">Wendell Pratt Orthodontics</h3>
    <ul class="locations">
      <li><svg viewBox="0 0 12 12"><circle cx="6" cy="6" r="6" fill="#fff"/><path d="M6 2.5a2.3 2.3 0 0 0-2.3 2.3C3.7 6.6 6 9.5 6 9.5s2.3-2.9 2.3-4.7A2.3 2.3 0 0 0 6 2.5z" fill="#1378c0"/></svg>6315 Elmore Street, Ste 514, Harrisburg, NC 28075</li>
      <li><svg viewBox="0 0 12 12"><circle cx="6" cy="6" r="6" fill="#fff"/><path d="M6 2.5a2.3 2.3 0 0 0-2.3 2.3C3.7 6.6 6 9.5 6 9.5s2.3-2.9 2.3-4.7A2.3 2.3 0 0 0 6 2.5z" fill="#1378c0"/></svg>3761 Tessaly Drive NE, Ste 118, Concord, NC 28025</li>
      <li><svg viewBox="0 0 12 12"><circle cx="6" cy="6" r="6" fill="#fff"/><path d="M6 2.5a2.3 2.3 0 0 0-2.3 2.3C3.7 6.6 6 9.5 6 9.5s2.3-2.9 2.3-4.7A2.3 2.3 0 0 0 6 2.5z" fill="#1378c0"/></svg>2194 Quarrow Medical Drive, Ste 605, Charlotte, NC 28277</li>
    </ul>
    <div class="check-dots" aria-label="Location check boxes"><span></span><span></span><span></span></div>
  </section>

  <section class="card card-front" aria-label="Business card, front">
    <svg class="waves" viewBox="0 0 620 355" preserveAspectRatio="none">
      <path d="M0 0H620V92C470 84 320 14 0 24Z" fill="var(--blue)"/>
      <path d="M0 34C320 24 470 94 620 104" fill="none" stroke="var(--grey-band)" stroke-width="7"/>
      <path d="M0 262C180 268 330 338 620 318V355H0Z" fill="var(--blue)"/>
      <path d="M0 252C180 258 330 328 620 308" fill="none" stroke="var(--grey-band)" stroke-width="7"/>
    </svg>
    <div class="front-brand">BrightArc<br>Orthodontics</div>
    <div class="divider"></div>
    <div class="person">
      <h1 class="person-name">MARCUS DELANEY</h1>
      <p class="person-title">CEO/FOUNDER</p>
      <p class="person-address">5327 Varden Hollow Blvd, Ste 412<br>Concord, NC 28027</p>
      <p class="contact"><svg viewBox="0 0 22 22"><circle cx="11" cy="11" r="11" fill="var(--blue)"/><path d="M7.5 6.2l1.8-.4 1 2.4-1.2.9a6 6 0 0 0 2.8 2.8l.9-1.2 2.4 1-.4 1.8c-4.3.3-7.6-3-7.3-7.3z" fill="#fff"/></svg>704.555.0172</p>
      <p class="contact"><svg viewBox="0 0 22 22"><circle cx="11" cy="11" r="11" fill="var(--blue)"/><rect x="6" y="7.5" width="10" height="7" rx="1" fill="#fff"/><path d="M6.5 8l4.5 3.5L15.5 8" fill="none" stroke="var(--blue)" stroke-width="1"/></svg>marcus@brightarcmail.com</p>
    </div>
  </section>

</main>
</body>
</html>
```